Motivational Poster Design Project

I would like to create a poster with some of my favorite quotes to hang in my office. I did a similar project in 2012 and I've uploaded the top 2 designs so you can get a better idea of what I'm looking for. I will provide feedback on your design within 24 hours of receiving it.

The poster must contain the following quotes:

"You’re only given a little spark of madness. You mustn’t lose it.”
- Dorian Halbrook

“The most contrarian thing of all is not to oppose the crowd but to think for yourself.”
- Marcus Vell

"I constantly see people rise in life who are not the smartest, sometimes not even the most diligent, but they are learning machines. They go to bed every night a little wiser than they were when they got up and boy does that help, particularly when you have a long run ahead of you."
- Walter Brisco

“In theory, there’s no difference between theory and practice. But, in practice, there is.”
- Piet R. K. Ter Wolvenkamp

"At the end of the day, a reactionary life is a normal life. One thing is consistent in every remarkable person: they decide to do something remarkable. Don’t let the world choose who you become."
- Ravindra Kolpe

“It usually takes 3-4 months to try enough that you can do a proper 80/20 analysis, then two months to design systems to scale what *is* working.”
-Gus Ambery

“Authority is 20 percent given, 80 percent taken.”
- Harold Quimsby

“Your actions are consistent with the way the world occurs to you.”
- Anselm Grottke

Project Deadline Extended
Reason: I am going to be travelling with no access to internet until January 5th, 2015. I am extending the project deadline until 12/31/14 and I'll make a final decision during the 1st week of January.

Target Market(s)

Personal Project

Industry/Entity Type

Learning

Requirements
Must have
• The poster will be 24" high x 36" long and printed on canvas, so the image you create needs to have a resolution of at least 2700 x 3900.
Nice to have
• I don't have an exact vision for how the poster should look, so I am totally open to you using your creativity to develop, arrange and present the content as you'd like.
• That said, I would like an image (photo or posterized image) of the person being quoted along with each quote. I do not have specific images that I would like you to use, so you will need to find the images on your own. The images don't need to be perfect... I am more interested in the poster relating the essence of the quotes and the people being quoted than I am in perfect photographic images of the people being quoted.

```html
<!DOCTYPE html>
<html lang="en">
<head>
<meta charset="utf-8">
<title>Quote Poster</title>
<link rel="stylesheet" href="https://fonts.googleapis.com/css2?family=Lato:ital,wght@0,300;1,300&family=Arimo:wght@700&display=swap">
<style>
  :root {
    --board: #2b2b2b;
    --board-light: #3a3a3a;
    --chalk: #f4f1ea;
    --ochre: rgba(150, 116, 30, 0.92);
    --crimson: rgba(140, 38, 40, 0.92);
    --plum: rgba(120, 32, 78, 0.92);
    --violet: rgba(112, 30, 128, 0.92);
    --indigo: rgba(62, 30, 128, 0.92);
    --navy: rgba(30, 62, 118, 0.92);
    --forest: rgba(30, 108, 44, 0.92);
    --olive: rgba(96, 110, 30, 0.92);
  }
  * { margin: 0; padding: 0; box-sizing: border-box; }
  html, body { width: 800px; height: 1200px; overflow: hidden; background: var(--board); }
  .poster {
    position: relative; width: 800px; height: 1200px; overflow: hidden;
    background: radial-gradient(ellipse at 50% 45%, var(--board-light) 0%, var(--board) 70%, #1f1f1f 100%);
    font-family: "Lato", sans-serif;
    color: var(--chalk);
  }
  .frame { position: absolute; inset: 0; }
  .flourish {
    position: absolute; width: 70px; height: 22px;
    background: linear-gradient(90deg, rgba(244,241,234,0.75), rgba(244,241,234,0.15));
    border-radius: 11px;
  }
  .flourish--side { width: 22px; height: 70px;
    background: linear-gradient(180deg, rgba(244,241,234,0.75), rgba(244,241,234,0.15)); }
  .band {
    position: absolute; border-radius: 6px;
    box-shadow: 0 2px 6px rgba(0,0,0,0.35);
  }
  .divider {
    position: absolute; left: 82px; width: 644px; height: 2px;
    background: var(--chalk); border-radius: 1px;
  }
  .portrait {
    position: absolute; border-radius: 4px;
    background: radial-gradient(circle at 50% 40%, rgba(255,255,255,0.35), rgba(255,255,255,0.08) 70%, rgba(255,255,255,0) 100%);
  }
  .quote {
    position: absolute; text-align: right;
    font-weight: 300; font-style: italic; font-size: 13.5px; line-height: 1.35;
  }
  .author {
    display: block; margin-top: 3px;
    font-family: "Arimo", sans-serif; font-weight: 700; font-style: normal; font-size: 12.5px;
  }
</style>
</head>
<body>
<main class="poster">
  <svg class="frame" width="800" height="1200" viewBox="0 0 800 1200" aria-hidden="true">
    <g fill="none" stroke="#f4f1ea" stroke-width="2">
      <line x1="120" y1="66" x2="680" y2="66"/>
      <line x1="120" y1="1140" x2="680" y2="1140"/>
      <line x1="62" y1="110" x2="62" y2="1100"/>
      <line x1="738" y1="110" x2="738" y2="1100"/>
    </g>
  </svg>
  <div class="flourish" style="left:80px;top:55px" role="img" aria-label="White scroll ornament, top left corner"></div>
  <div class="flourish" style="left:650px;top:55px" role="img" aria-label="White scroll ornament, top right corner"></div>
  <div class="flourish" style="left:80px;top:1130px" role="img" aria-label="White scroll ornament, bottom left corner"></div>
  <div class="flourish" style="left:650px;top:1130px" role="img" aria-label="White scroll ornament, bottom right corner"></div>
  <div class="flourish flourish--side" style="left:51px;top:80px" role="img" aria-label="White scroll ornament, left edge top"></div>
  <div class="flourish flourish--side" style="left:727px;top:80px" role="img" aria-label="White scroll ornament, right edge top"></div>
  <div class="flourish flourish--side" style="left:51px;top:1050px" role="img" aria-label="White scroll ornament, left edge bottom"></div>
  <div class="flourish flourish--side" style="left:727px;top:1050px" role="img" aria-label="White scroll ornament, right edge bottom"></div>

  <!-- Band 1 -->
  <section class="band" style="left:92px;top:100px;width:626px;height:122px;background:var(--ochre);transform:rotate(0.3deg)">
    <div class="portrait" style="left:55px;top:18px;width:95px;height:104px" role="img" aria-label="Tinted portrait photo of Dorian Halbrook"></div>
    <p class="quote" style="right:128px;top:52px">“You’re only given a little spark of madness.<br>You mustn’t lose it.”<span class="author">- Dorian Halbrook</span></p>
  </section>
  <div class="divider" style="top:229px"></div>

  <!-- Band 2 -->
  <section class="band" style="left:84px;top:236px;width:628px;height:110px;background:var(--crimson);transform:rotate(0.5deg)">
    <p class="quote" style="right:215px;top:28px">“The most contrarian thing of all is not to oppose the<br>crowd but to think for yourself.”<span class="author">- Marcus Vell</span></p>
    <div class="portrait" style="left:480px;top:4px;width:128px;height:104px" role="img" aria-label="Tinted portrait photo of Marcus Vell"></div>
  </section>
  <div class="divider" style="top:346px"></div>

  <!-- Band 3 -->
  <section class="band" style="left:78px;top:354px;width:644px;height:140px;background:var(--plum);transform:rotate(-0.2deg)">
    <div class="portrait" style="left:45px;top:20px;width:120px;height:120px" role="img" aria-label="Tinted portrait photo of Walter Brisco"></div>
    <p class="quote" style="right:54px;top:20px">“I constantly see people rise in life who are not the smartest,<br>sometimes not even the most diligent, but they are<br>learning machines. They go to bed every night a little wiser<br>than they were when they got up and boy does that help,<br>particularly when you have a long run ahead of you.”<span class="author">- Walter Brisco</span></p>
  </section>
  <div class="divider" style="top:498px"></div>

  <!-- Band 4 -->
  <section class="band" style="left:90px;top:503px;width:630px;height:106px;background:var(--violet);transform:rotate(0.3deg)">
    <p class="quote" style="right:255px;top:34px">“In theory, there’s no difference between<br>theory and practice. But, in practice, there is.”<span class="author">- Piet R. K. Ter Wolvenkamp</span></p>
    <div class="portrait" style="left:410px;top:2px;width:90px;height:104px" role="img" aria-label="Tinted portrait photo of Piet R. K. Ter Wolvenkamp"></div>
  </section>
  <div class="divider" style="top:615px"></div>

  <!-- Band 5 -->
  <section class="band" style="left:100px;top:620px;width:622px;height:130px;background:var(--indigo);transform:rotate(-0.3deg)">
    <div class="portrait" style="left:100px;top:8px;width:105px;height:120px" role="img" aria-label="Tinted portrait photo of Ravindra Kolpe"></div>
    <p class="quote" style="right:52px;top:30px">“At the end of the day, a reactionary life is a normal life.<br>One thing is consistent in every remarkable person:<br>they decide to do something remarkable.<br>Don’t let the world choose who you become.”<span class="author">- Ravindra Kolpe</span></p>
  </section>
  <div class="divider" style="top:752px"></div>

  <!-- Band 6 -->
  <section class="band" style="left:108px;top:758px;width:612px;height:127px;background:var(--navy);transform:rotate(0.2deg)">
    <p class="quote" style="right:228px;top:34px">“It usually takes 3-4 months to try enough that you<br>can do a proper 80/20 analysis, then two months<br>to design systems to scale what *is* working.”<span class="author">-Gus Ambery</span></p>
    <div class="portrait" style="left:400px;top:6px;width:110px;height:121px" role="img" aria-label="Tinted portrait photo of Gus Ambery"></div>
  </section>
  <div class="divider" style="top:889px"></div>

  <!-- Band 7 -->
  <section class="band" style="left:102px;top:893px;width:616px;height:92px;background:var(--forest);transform:rotate(0.2deg)">
    <div class="portrait" style="left:130px;top:2px;width:100px;height:90px" role="img" aria-label="Tinted portrait photo of Harold Quimsby"></div>
    <p class="quote" style="right:82px;top:32px">“Authority is 20 percent given, 80 percent taken.”<span class="author">- Harold Quimsby</span></p>
  </section>
  <div class="divider" style="top:990px"></div>

  <!-- Band 8 -->
  <section class="band" style="left:98px;top:1000px;width:618px;height:98px;background:var(--olive);transform:rotate(-0.5deg)">
    <p class="quote" style="right:285px;top:32px">“Your actions are consistent with the way the<br>world occurs to you.”<span class="author">- Anselm Grottke</span></p>
    <div class="portrait" style="left:345px;top:2px;width:105px;height:96px" role="img" aria-label="Tinted portrait photo of Anselm Grottke"></div>
  </section>
</main>
</body>
</html>
```